Einladung zum Geburtstag
Einladung zu einer Geburtstagsparty von zwei "Mädels", die zusammen 99 Jahre jung werden.
Eine wird 55 (25.8.) die andere 44. (24.8.) - alles "Schnapszahlen".
Es soll eine kleine Party tagsüber für die Arbeitskollegen werden, mit Imbiss und Umtrunk. Termin für die Feier ist der 25.8. ab 14h.
Die Einladung soll sowohl gedruckt als auch per Mail verschickt werden können.

```html
<!DOCTYPE html>
<html lang="de">
<head>
<meta charset="utf-8">
<title>Einladung Gartenparty</title>
<link rel="stylesheet" href="https://fonts.googleapis.com/css2?family=Jura:wght@500;600&family=Pirata+One&display=swap">
<style>
  :root {
    --paper: #ffffff;
    --band-left: #ea6a24;
    --band-mid: #ee7f22;
    --band-right: #f4a51e;
    --accent: #e4471c;
    --text-light: #ffffff;
    --lettering: #ec7a1e;
  }
  html, body {
    margin: 0;
    padding: 0;
    width: 1200px;
    height: 571px;
    overflow: hidden;
    background: var(--paper);
  }
  .invitation {
    position: relative;
    width: 1200px;
    height: 571px;
    background: var(--paper);
    font-family: "Jura", sans-serif;
    font-weight: 600;
  }
  .band {
    position: absolute;
    left: 0;
    top: 114px;
    width: 1146px;
    height: 416px;
    border-top-right-radius: 10px;
    border-bottom-right-radius: 10px;
    background: linear-gradient(90deg, var(--band-left) 0%, var(--band-mid) 45%, var(--band-right) 100%);
  }
  .dot-field {
    position: absolute;
    left: 0;
    top: 114px;
    width: 700px;
    height: 416px;
    background: linear-gradient(90deg, rgba(255,255,255,0.8) 0%, rgba(255,255,255,0.5) 14%, rgba(255,255,255,0.2) 30%, rgba(255,255,255,0.12) 55%, rgba(255,255,255,0) 100%);
  }
  .bubbles {
    position: absolute;
    left: 290px;
    top: 420px;
    width: 860px;
    height: 110px;
    background: radial-gradient(ellipse closest-side at 50% 100%, rgba(255,255,255,0.28) 0%, rgba(255,255,255,0) 100%);
  }
  .tropical-scene {
    position: absolute;
    left: 600px;
    top: 30px;
    width: 600px;
    height: 500px;
    background: radial-gradient(ellipse closest-side at 55% 55%, #f8c72a 0%, #f4a820 45%, rgba(240,140,34,0.5) 75%, rgba(240,140,34,0) 100%);
  }
  .heading {
    position: absolute;
    left: 184px;
    top: -6px;
    margin: 0;
    font-family: "Pirata One", cursive;
    font-weight: 400;
    font-size: 118px;
    line-height: 1.2;
    color: var(--lettering);
    letter-spacing: 1px;
  }
  .message {
    position: absolute;
    left: 251px;
    top: 188px;
    color: var(--text-light);
    font-size: 21px;
    line-height: 40px;
    white-space: nowrap;
    margin: 0;
  }
  .message .line { display: block; height: 40px; }
  .hl { color: var(--accent); line-height: 1; }
  .big { font-size: 40px; }
  .party { font-size: 29px; }
  .day { font-size: 24px; }
  .date { font-size: 33px; letter-spacing: 1px; margin: 0 6px 0 2px; }
  .time { font-size: 29px; margin-left: 6px; }
  .hosts {
    position: absolute;
    left: 0;
    width: 1022px;
    top: 370px;
    text-align: center;
    font-size: 30px;
    line-height: 1;
    color: var(--accent);
    margin: 0;
  }
  .hosts .amp { color: var(--text-light); }
</style>
</head>
<body>
  <main class="invitation">
    <div class="band"></div>
    <div class="dot-field" role="img" aria-label="Weißes Punkteraster, das nach rechts ausläuft"></div>
    <div class="bubbles" role="img" aria-label="Weiße Kreise als Blasenmuster am unteren Rand"></div>
    <div class="tropical-scene" role="img" aria-label="Illustration mit Palmen, Martiniglas, Cocktail mit Strohhalm und Zitronenscheiben"></div>

    <h1 class="heading">Einladung</h1>

    <p class="message">
      <span class="line">Zusammen werden wir <span class="hl big">99</span>! Dies wollen wir bei</span>
      <span class="line">gutem Wetter mit Euch bei einer Garten<span class="hl party">party</span> am</span>
      <span class="line"><span class="hl day">Donnerstag</span>, den <span class="hl date">25.08.2011</span> ab <span class="hl time">14 Uhr</span></span>
      <span class="line">feiern! Wir freuen uns auf Euer Kommen!</span>
    </p>

    <p class="hosts">Merle <span class="amp">&amp;</span> Ilka</p>
  </main>
</body>
</html>
```